Wendmar Digital - Layout Design

We need a web design for a new company based in Australia, called "Wendmar Digital". We develop innovative custom web applications for Out Of Home, and Media companies.
Our initial website is a one page type of site. I've created a simple wireframe to show you what we need: https://sketchplot.example/qT4mZ9
Here is a layout reference: http://fernloft.example/
( note - the designs needs to follow our branding guidelines (attached).
The top feature could be just solid color or an abstract subtle pattern or illustration that conveys the specialization of our business in the area of out of home, map, data.
In the attachment you will also find some images added for the work section.
Media and Advertising
Digital
1 page

```html
<!DOCTYPE html>
<html lang="en">
<head>
<meta charset="utf-8">
<title>Wendmar Digital</title>
<link href="https://fonts.googleapis.com/css2?family=Lato:wght@400;700;900&display=swap" rel="stylesheet">
<style>
:root{
  --ink:#2a2a35;
  --muted:#4a4a55;
  --night:#2b1c4c;
  --night-deep:#231640;
  --accent:#f29a1f;
  --teal:#25a8c6;
  --rule:#d9d9df;
  --white:#ffffff;
}
*{box-sizing:border-box;margin:0;padding:0}
html,body{width:1200px;height:2208px;overflow:hidden;background:var(--white)}
body{font-family:"Lato",Arial,sans-serif;color:var(--ink);position:relative}

.site-header{position:absolute;top:0;left:0;width:1200px;height:60px;background:var(--night-deep);display:flex;align-items:center;justify-content:space-between;padding:0 60px 0 44px;z-index:2}
.brand{display:flex;align-items:center;gap:10px;color:var(--white);font-size:30px;font-weight:700;letter-spacing:-.5px}
.brand-dot{width:14px;height:14px;border-radius:50%;background:var(--teal)}
.nav{display:flex;gap:0}
.nav a{color:var(--white);text-decoration:none;font-size:12px;font-weight:700;letter-spacing:.5px;padding:22px 14px}
.nav a.is-active{background:var(--teal)}

.hero{position:absolute;top:60px;left:0;width:1200px;height:500px;background:
  radial-gradient(circle at 78% 40%,rgba(236,72,153,.55),transparent 40%),
  radial-gradient(circle at 15% 85%,rgba(37,168,198,.55),transparent 40%),
  linear-gradient(125deg,#1d6fb8 0%,#3a2e8f 35%,#6b2f9c 60%,#c43d8e 85%,#e0557a 100%)}
.hero-copy{position:absolute;left:44px;top:110px;color:var(--white)}
.hero-title{font-size:36px;font-weight:900;letter-spacing:-.3px}
.hero-sub{font-size:13px;line-height:20px;margin-top:10px;opacity:.9}
.hero-dots{position:absolute;left:36px;bottom:36px;display:flex;gap:10px}
.hero-dots span{width:14px;height:14px;border-radius:50%;background:rgba(255,255,255,.55)}
.hero-dots span.is-current{background:var(--accent)}

.content{position:absolute;top:560px;left:0;width:1200px;text-align:center}
.section-title{font-size:30px;font-weight:700;color:var(--ink);line-height:36px}
.section-title em{font-style:normal;color:var(--accent)}
.lede{font-size:13px;line-height:20px;color:var(--muted);width:740px;margin:0 auto}
.why{padding-top:28px}
.why .lede{margin-top:12px}
.team{margin-top:32px}
.team > .lede{margin-top:10px}
.person{margin-top:22px}
.avatar{width:68px;height:68px;border-radius:50%;background:linear-gradient(135deg,#2fb7d3,#1b8aa8);border:3px solid #bfe7f1;margin:0 auto}
.person-name{font-size:11px;font-weight:700;color:var(--teal);letter-spacing:.6px;margin-top:8px}
.person .lede{margin-top:8px}
.advisors{margin-top:34px}
.services{margin-top:34px}
.services .lede{margin-top:8px}
.divider{width:1040px;height:1px;background:var(--rule);margin:6px auto 0}
.experience{margin-top:30px}
.project{display:flex;gap:36px;width:580px;margin:0 auto;text-align:left}
.project:first-of-type{margin-top:18px}
.project + .project{margin-top:20px}
.project-media{flex:0 0 260px}
.shot{height:156px;border-radius:2px}
.shot.outdoor{background:linear-gradient(135deg,#e7eef5,#f1a24a 55%,#7d6a95)}
.shot.geo{height:90px;background:linear-gradient(135deg,#f3c85a,#e0632f 50%,#3c86b8)}
.project-label{font-size:11px;color:var(--ink);margin-top:6px}
.project-text{font-size:13px;line-height:20px;color:var(--muted)}
.project-text p + p{margin-top:12px}

.site-footer{position:absolute;left:0;top:2058px;width:1200px;height:150px;background:var(--night);color:var(--white);text-align:center;padding-top:14px}
.footer-title{font-size:15px;font-weight:700;letter-spacing:.6px}
.footer-intro{font-size:13px;margin-top:4px}
.contact-list{width:300px;margin:10px auto 0;text-align:left;font-size:11px;line-height:16px;color:#c9c2df}
.contact-row{display:flex;gap:10px;align-items:flex-start;margin-bottom:5px}
.contact-row svg{flex:0 0 16px;margin-top:1px}
</style>
</head>
<body>

<header class="site-header">
  <div class="brand"><span>Wendmar Digital</span><span class="brand-dot"></span></div>
  <nav class="nav">
    <a href="#about">ABOUT US</a>
    <a href="#team">TEAM</a>
    <a href="#services" class="is-active">SERVICES</a>
    <a href="#experience">EXPERIENCE</a>
    <a href="#contact">CONTACT</a>
  </nav>
</header>

<section class="hero" role="img" aria-label="Abstract faceted colour field with map pins rising from circular data rings">
  <div class="hero-copy">
    <h1 class="hero-title">Information. Insight. Action.</h1>
    <p class="hero-sub">Our clients connected with their data in a new way.<br>Turning location data into insight you can act upon.</p>
  </div>
  <div class="hero-dots"><span class="is-current"></span><span></span><span></span><span></span></div>
</section>

<main class="content">
  <section class="why" id="about">
    <h2 class="section-title">Why Choose <em>Us?</em></h2>
    <p class="lede">We are Wendmar Digital. A team of innovators, thinkers and doers working collaboratively toward our goal.<br>With decades of experience between us from a variety of sources.<br>Wendmar Digital is a business focused on helping organisations gain more value from information, through insight and action.</p>
  </section>

  <section class="team" id="team">
    <h2 class="section-title">Key <em>Team</em></h2>
    <p class="lede">Sed ut perspiciatis unde omnis iste natus error sit voluptatem accusantium doloremque laudantium, totam rem aperiam, eaque ipsa quae ab illo inventore veritatis et quasi architecto beatae vitae dicta sunt explicabo.</p>
    <div class="person">
      <div class="avatar" role="img" aria-label="Portrait of Daniel Harcourt"></div>
      <p class="person-name">DANIEL HARCOURT - CEO</p>
      <p class="lede">Sed ut perspiciatis unde omnis iste natus error sit voluptatem accusantium doloremque laudantium, totam rem aperiam, eaque ipsa quae ab illo inventore veritatis et quasi architecto beatae vitae dicta sunt explicabo.</p>
    </div>
    <div class="person">
      <div class="avatar" role="img" aria-label="Portrait of Brian Okafor"></div>
      <p class="person-name">BRIAN OKAFOR - CTO</p>
      <p class="lede">Sed ut perspiciatis unde omnis iste natus error sit voluptatem accusantium doloremque laudantium, totam rem aperiam, eaque ipsa quae ab illo inventore veritatis et quasi architecto beatae vitae dicta sunt explicabo.</p>
    </div>
    <div class="person">
      <div class="avatar" role="img" aria-label="Portrait of Stephen Lowry"></div>
      <p class="person-name">STEPHEN LOWRY - EXECUTIVE PARTNER</p>
    </div>
  </section>

  <section class="advisors">
    <h2 class="section-title">Board <em>of Advisors</em></h2>
    <div class="person">
      <div class="avatar" role="img" aria-label="Portrait of Leanne Whitby"></div>
      <p class="person-name">LEANNE WHITBY</p>
      <p class="lede">Sed ut perspiciatis unde omnis iste natus error sit voluptatem accusantium doloremque laudantium, totam rem aperiam, eaque ipsa quae ab illo inventore veritatis et quasi architecto beatae vitae dicta sunt explicabo.</p>
    </div>
  </section>

  <section class="services" id="services">
    <h2 class="section-title">Services</h2>
    <div class="divider"></div>
    <p class="lede">Sed ut perspiciatis unde omnis iste natus error sit voluptatem accusantium doloremque laudantium, totam rem aperiam, eaque ipsa quae ab illo inventore veritatis et quasi architecto beatae vitae dicta sunt explicabo.</p>
  </section>

  <section class="experience" id="experience">
    <h2 class="section-title">Experience</h2>
    <div class="divider"></div>
    <div class="project">
      <div class="project-media">
        <div class="shot outdoor" role="img" aria-label="Kestrel Outdoor campaign planning app shown on a laptop"></div>
        <p class="project-label">Kestrel Outdoor</p>
      </div>
      <div class="project-text">
        <p>A bold and progressive website for Australia and New Zealand that highlights Kestrel Outdoor’s exciting new branding and extensive asset inventory.</p>
        <p>Interactive and practical campaign planning tools have helped to position Kestrel as a forward-thinking player in the OOH industry.</p>
      </div>
    </div>
    <div class="project">
      <div class="project-media">
        <div class="shot geo" role="img" aria-label="Farwander geography learning app screens"></div>
        <p class="project-label">Farwander</p>
      </div>
      <div class="project-text">
        <p>Farwander is a world-first geography learning application created with the use of Atlasly Maps.</p>
        <p>The user creates a learning experience personalised to the user. As users study and memorise different countries they are awarded points and badges.</p>
      </div>
    </div>
  </section>
</main>

<footer class="site-footer" id="contact">
  <h2 class="footer-title">CONTACT</h2>
  <p class="footer-intro">Curious about what we can do to help your organisation? Then please get in touch.</p>
  <div class="contact-list">
    <div class="contact-row">
      <svg width="16" height="12" viewBox="0 0 16 12"><rect x="0.5" y="0.5" width="15" height="11" fill="none" stroke="#c9c2df"/><path d="M1 1l7 6 7-6" fill="none" stroke="#c9c2df"/></svg>
      <span>info@wendmardigital.example</span>
    </div>
    <div class="contact-row">
      <svg width="16" height="16" viewBox="0 0 16 16"><path d="M8 1a5 5 0 0 0-5 5c0 4 5 9 5 9s5-5 5-9a5 5 0 0 0-5-5z" fill="none" stroke="#c9c2df"/><circle cx="8" cy="6" r="1.8" fill="#c9c2df"/></svg>
      <span>Wendmar Digital Pty Ltd | Suite 4, Level 7 | 18 Harbour Lane<br>Sydney NSW 2000, Australia</span>
    </div>
    <div class="contact-row">
      <svg width="16" height="16" viewBox="0 0 16 16"><path d="M4 1.5l2.5 3-1.5 1.8a9 9 0 0 0 4.7 4.7L11.5 9.5l3 2.5-1.7 2.3C7.5 14 2 8.5 1.7 3.2z" fill="none" stroke="#c9c2df"/></svg>
      <span>02 5550 1947</span>
    </div>
  </div>
</footer>

</body>
</html>
```